Quorvel Marketing & Design needs a Wordpress website

We need a wordpress design for a new marketing and design company in Australia called 'Quorvel Marketing & Design". The website needs to be responsive, modern, and attract new customers. It needs to be unique and different. We provide marketing and design solutions for small businesses from consulting, to flyer distribution to Facebook ads etc. We would like to see designs that use the Quorvel logo colours. The final design should communicate professionalism, creativity & growth. It needs to stand out from the crowd.

Target Market(s)

Small Business who need a marketing freelancer to help them grow

Industry/Entity Type

Marketing

Number of Pages Required

3 page

Requirements
Must have
• Home page, services page & contact page

```html
<!DOCTYPE html>
<html lang="en">
<head>
<meta charset="utf-8">
<title>Quorvel Marketing &amp; Design</title>
<link href="https://fonts.googleapis.com/css2?family=Open+Sans:wght@400;600;700&family=Roboto+Slab:wght@400;700&display=swap" rel="stylesheet">
<style>
:root{
  --pink:#e5127d;
  --pink-dark:#c10b68;
  --navy:#2a2460;
  --navy-deep:#1d1947;
  --ink:#222033;
  --muted:#7a7a86;
  --grey-bg:#ededf0;
  --white:#ffffff;
  --line:#d6d6dc;
}
*{box-sizing:border-box;margin:0;padding:0}
html,body{width:813px;height:1200px;overflow:hidden}
body{font-family:"Open Sans",Arial,sans-serif;color:var(--ink);background:var(--white);position:relative}
.slab{font-family:"Roboto Slab",Georgia,serif}

/* header */
.site-header{position:absolute;top:0;left:0;width:813px;height:92px;background:var(--white);box-shadow:0 2px 6px rgba(0,0,0,.12);z-index:3}
.brand{position:absolute;left:70px;top:16px;display:flex;align-items:center;gap:10px}
.brand-dot{width:48px;height:48px;border-radius:50%;background:var(--pink)}
.brand-name{font-family:"Roboto Slab",Georgia,serif;font-weight:700;font-size:26px;color:var(--ink);line-height:1}
.brand-sub{font-size:10px;font-weight:600;color:var(--pink);letter-spacing:1.5px;margin-top:4px}
.top-contact{position:absolute;right:60px;top:10px;display:flex;gap:22px;font-size:10px;color:var(--ink)}
.top-contact span{display:flex;align-items:center;gap:5px}
.main-nav{position:absolute;right:45px;top:44px;display:flex;font-size:12px}
.main-nav a{color:var(--ink);text-decoration:none;padding:0 20px;border-left:1px solid var(--line)}
.main-nav a:first-child{border-left:none}

/* hero */
.hero{position:absolute;top:92px;left:0;width:813px;height:300px;background:linear-gradient(135deg,#3a2f7a 0%,var(--navy) 55%,var(--navy-deep) 100%)}
.hero-visual{position:absolute;left:45px;top:14px;width:200px;height:190px;border-radius:6px;background:linear-gradient(160deg,#f3b341,#3b6bd6 60%,#1f1f2e)}
.hero-copy{position:absolute;left:470px;top:62px;width:300px;color:var(--white)}
.hero-copy h1{font-family:"Roboto Slab",Georgia,serif;font-size:27px;font-weight:700;margin-bottom:10px}
.hero-copy p{font-size:10px;line-height:1.55;opacity:.9}
.hero-actions{position:absolute;left:525px;top:178px;display:flex;gap:10px}
.btn{display:inline-block;font-size:11px;font-weight:600;color:var(--white);padding:7px 14px;border-radius:2px}
.btn-dark{background:var(--navy-deep)}
.btn-pink{background:var(--pink)}

/* service boxes */
.services{position:absolute;top:342px;left:85px;width:643px;display:flex;gap:12px;z-index:2}
.service{flex:1;height:225px;background:var(--pink);color:var(--white);text-align:center;padding:22px 18px 0}
.service.alt{background:var(--navy-deep)}
.service-icon{width:50px;height:50px;border-radius:50%;background:var(--white);margin:0 auto 18px;display:flex;align-items:center;justify-content:center}
.service h3{font-family:"Roboto Slab",Georgia,serif;font-size:20px;font-weight:400;margin-bottom:10px}
.service p{font-size:9px;line-height:1.5;opacity:.92}

/* about */
.about{position:absolute;top:392px;left:0;width:813px;height:350px;background:var(--grey-bg);padding-top:204px;text-align:center}
.section-title{font-family:"Roboto Slab",Georgia,serif;font-size:20px;color:var(--ink);display:inline-block;position:relative;padding:0 0 8px}
.section-title::before,.section-title::after{content:"";position:absolute;top:13px;width:140px;height:1px;background:var(--line)}
.section-title::before{right:calc(100% + 14px)}
.section-title::after{left:calc(100% + 14px)}
.about p{width:620px;margin:10px auto 0;font-size:10px;line-height:1.7;color:var(--muted)}

/* testimonials */
.testimonials{position:absolute;top:742px;left:0;width:813px;height:225px;text-align:center;padding-top:20px}
.quotes{display:flex;gap:40px;justify-content:center;margin-top:22px}
.quote{width:320px;display:flex;gap:14px;text-align:left}
.avatar{width:62px;height:62px;border-radius:50%;background:linear-gradient(135deg,#c9a58e,#6d5b52);flex:none;border:3px solid var(--white);box-shadow:0 0 0 1px var(--line)}
.quote-body{border:1px solid var(--line);padding:10px 12px;font-size:9px;line-height:1.55;color:var(--muted)}
.quote-name{font-size:10px;color:var(--muted);margin-top:10px;text-align:center}

/* contact */
.contact{position:absolute;top:967px;left:0;width:813px;height:200px;background:linear-gradient(135deg,#3a2f7a,var(--navy-deep));color:var(--white)}
.contact h2{position:absolute;left:75px;top:22px;font-family:"Roboto Slab",Georgia,serif;font-size:20px;font-weight:400}
.contact-info{position:absolute;left:75px;top:58px;width:280px;font-size:9px;line-height:1.6;opacity:.92}
.contact-info .row{display:flex;gap:8px;margin-top:8px;align-items:flex-start}
.contact-info strong{font-weight:700}
.contact-form{position:absolute;left:430px;top:20px;width:325px}
.field{display:flex;align-items:center;margin-bottom:8px}
.field label{width:100px;font-size:9px}
.field .input{flex:1;height:20px;background:var(--white);border-radius:2px;font-size:9px;color:var(--muted);padding:4px 6px}
.field.msg{align-items:flex-start}
.field.msg .input{height:70px}
.submit{margin-left:100px;background:var(--pink);font-size:9px;font-weight:700;padding:5px 12px;display:inline-block}

/* bottom bar */
.bottom-bar{position:absolute;top:1167px;left:0;width:813px;height:33px;background:var(--navy-deep);color:#b7b3d6;font-size:8px;display:flex;align-items:center;justify-content:space-between;padding:0 60px 0 75px}
.social{display:flex;gap:6px}
.social span{width:16px;height:16px;background:#3d3878}
</style>
</head>
<body>

<header class="site-header">
  <div class="brand">
    <div class="brand-dot"></div>
    <div>
      <div class="brand-name">Quorvel</div>
      <div class="brand-sub">MARKETING &amp; DESIGN</div>
    </div>
  </div>
  <div class="top-contact">
    <span><svg width="9" height="9" viewBox="0 0 24 24"><path fill="#e5127d" d="M6.6 10.8a15 15 0 006.6 6.6l2.2-2.2c.3-.3.7-.4 1-.2 1.1.4 2.3.6 3.6.6.6 0 1 .4 1 1V20c0 .6-.4 1-1 1C10.6 21 3 13.4 3 4c0-.6.4-1 1-1h3.5c.6 0 1 .4 1 1 0 1.3.2 2.5.6 3.6.1.3 0 .7-.2 1z"/></svg>123-555-0142</span>
    <span><svg width="10" height="8" viewBox="0 0 24 18"><rect width="24" height="18" rx="2" fill="#e5127d"/><path d="M1 2l11 8 11-8" stroke="#fff" stroke-width="2" fill="none"/></svg>info@quorvel.com</span>
  </div>
  <nav class="main-nav">
    <a href="#">Home</a><a href="#">About Us</a><a href="#">Services</a><a href="#">Contact Us</a>
  </nav>
</header>

<section class="hero">
  <div class="hero-visual" role="img" aria-label="Stack of devices and print pieces showing branding work"></div>
  <div class="hero-copy">
    <h1>Build Amazing Branding</h1>
    <p>Are you looking for some marketing help for your business? Have you started your own business and ready to take the plunge in getting your name out there? You are in the right place!</p>
  </div>
  <div class="hero-actions">
    <span class="btn btn-dark">Learn More</span>
    <span class="btn btn-pink">Get Free Quote</span>
  </div>
</section>

<section class="about">
  <h2 class="section-title">About To Quorvel</h2>
  <p>Looking for some marketing expertise for a new business that you have just started and are ready to take the plunge in getting your name out there? You have come to the right place! It might just be that you want some solid marketing advice and direction to point you in the right way, or it might be that you need hands on help to grow. Whatever you decide is best for you, we are here to support every step. At Quorvel we understand that small business is the heart of our community and we build plans that fit your budget and your goals.</p>
</section>

<div class="services">
  <div class="service">
    <div class="service-icon"><svg width="24" height="24" viewBox="0 0 24 24"><rect x="3" y="3" width="8" height="8" fill="#e5127d"/><rect x="13" y="3" width="8" height="8" fill="#2a2460"/><rect x="3" y="13" width="8" height="8" fill="#2a2460"/><rect x="13" y="13" width="8" height="8" fill="#e5127d"/></svg></div>
    <h3>Just starting up?</h3>
    <p>Congratulations, you made the first step to success. Now you need to tell the world about it and we will help you craft a plan that works.</p>
  </div>
  <div class="service alt">
    <div class="service-icon"><svg width="24" height="24" viewBox="0 0 24 24"><circle cx="12" cy="8" r="4" fill="#2a2460"/><path d="M4 21c0-4.4 3.6-7 8-7s8 2.6 8 7z" fill="#e5127d"/></svg></div>
    <h3>Need a marketing</h3>
    <p>If your business has been running for a while and you need to boost your sales, then we can help with flyers, ads and social media plans.</p>
  </div>
  <div class="service">
    <div class="service-icon"><svg width="24" height="24" viewBox="0 0 24 24"><path d="M3 4h14v10H8l-5 4z" fill="#e5127d"/><path d="M19 8h2v12l-4-3h-8v-2h10z" fill="#2a2460"/></svg></div>
    <h3>Consulting &amp; Advise</h3>
    <p>If you just want some solid advice on marketing tips and direction, we can sit down with you and share our best ideas for growth.</p>
  </div>
</div>

<section class="testimonials">
  <h2 class="section-title">Client Testimonial</h2>
  <div class="quotes">
    <div>
      <div class="quote">
        <div class="avatar" role="img" aria-label="Portrait of client"></div>
        <div class="quote-body">“ The team gave our small shop a clear plan and fresh flyers. Sales went up within weeks and our customers noticed the new look straight away. ”</div>
      </div>
      <div class="quote-name">Mr. Liam Carter</div>
    </div>
    <div>
      <div class="quote">
        <div class="avatar" role="img" aria-label="Portrait of client"></div>
        <div class="quote-body">“ Friendly, creative and quick to respond. Our social ads now bring steady enquiries and we finally feel confident about our marketing. ”</div>
      </div>
      <div class="quote-name">Miss Ava Porter</div>
    </div>
  </div>
</section>

<section class="contact">
  <h2>Get in touch with us</h2>
  <div class="contact-info">
    <p>We would love to hear about your business. Send us a message and we will reply within one day.</p>
    <div class="row"><svg width="9" height="11" viewBox="0 0 24 30"><path d="M12 0a10 10 0 0110 10c0 8-10 20-10 20S2 18 2 10A10 10 0 0112 0z" fill="#e5127d"/></svg><div><strong>Quorvel</strong><br>12 Harbour Lane, Suite 4<br>Sydney NSW 2000</div></div>
    <div class="row"><svg width="9" height="9" viewBox="0 0 24 24"><path fill="#e5127d" d="M6.6 10.8a15 15 0 006.6 6.6l2.2-2.2c.3-.3.7-.4 1-.2 1.1.4 2.3.6 3.6.6.6 0 1 .4 1 1V20c0 .6-.4 1-1 1C10.6 21 3 13.4 3 4c0-.6.4-1 1-1h3.5c.6 0 1 .4 1 1 0 1.3.2 2.5.6 3.6.1.3 0 .7-.2 1z"/></svg>123-555-0142</div>
    <div class="row"><svg width="10" height="8" viewBox="0 0 24 18"><rect width="24" height="18" rx="2" fill="#e5127d"/><path d="M1 2l11 8 11-8" stroke="#fff" stroke-width="2" fill="none"/></svg>info@quorvel.com</div>
  </div>
  <div class="contact-form">
    <div class="field"><label>Name</label><div class="input">Name</div></div>
    <div class="field"><label>Email</label><div class="input">Email</div></div>
    <div class="field msg"><label>Message</label><div class="input">Message</div></div>
    <span class="submit">SUBMIT</span>
  </div>
</section>

<footer class="bottom-bar">
  <span>Copyright © 2024 Quorvel. All rights reserved.</span>
  <div class="social"><span></span><span></span><span></span><span></span></div>
</footer>

</body>
</html>
```